Brand Design/Redesign

Design and/or redesign an identity for product and organisation
Create visual identity (colours, fonts), website, mobile app, web application, online campaigns, social media.

I have given a sample wireframe for you to use so that we can really get a sense of the colour palette you are choosing and how it will look in a live context.

Considerations when Choosing:
Brand is for Gen Z -
With a particular focus on 16 - 18 years old.

There will be a commercial portal for Business to use also.

Please outline in a short paragraph why you choose the colours and their relationship to our target audience.

Selected winner to produce Brand Identity Document

Please see document attached.

Target Market(s)

Gen Z 16 - 18 yearolds

Industry/Entity Type

Social Media

Requirements
Must have
• Colour Palette & Font Selections, Visual of Colour Palette & Winner to produce Brand Identity Doc
Nice to have
• Really Cool, Edgy and Appeal to aYoung Audience
Should not have
• A corporate feel to it

```html
<!DOCTYPE html>
<html lang="en">
<head>
<meta charset="utf-8">
<title>Kivora – App Screens</title>
<link rel="stylesheet" href="https://fonts.googleapis.com/css2?family=Oswald:wght@500;600;700&family=Roboto:wght@400;500;700&display=swap">
<style>
  :root{
    --bg:#a63ef5;
    --cyan:#06d9e8;
    --blue:#5d8ff3;
    --violet:#a24cf6;
    --magenta:#f21ad0;
    --indigo:#2a0a8a;
    --ink:#2b2b2b;
    --soft:#f6f6f7;
    --field:#ececee;
    --white:#ffffff;
    --head:'Oswald', sans-serif;
    --body:'Roboto', sans-serif;
  }
  *{box-sizing:border-box;margin:0;padding:0}
  html,body{width:1200px;height:805px;overflow:hidden}
  body{background:var(--bg);position:relative;font-family:var(--body)}
  .screen{position:absolute;width:295px;height:650px;top:74px;border-radius:24px;overflow:hidden}
  .abs{position:absolute}

  /* Login screen */
  .login{left:94px;background:var(--soft)}
  .login__wave{position:absolute;left:0;top:0}
  .login__brand{position:absolute;top:78px;width:100%;text-align:center;font-family:var(--head);font-weight:700;font-size:50px;letter-spacing:2px;color:var(--white)}
  .login__title{position:absolute;top:318px;width:100%;text-align:center;font-family:var(--head);font-weight:700;font-size:33px;background:linear-gradient(90deg,var(--cyan),var(--violet));-webkit-background-clip:text;background-clip:text;color:transparent}
  .field{position:absolute;left:39px;width:218px;height:30px;border-radius:15px;background:var(--field);font-size:9.5px;color:#666;padding-left:18px;line-height:30px}
  .field svg{position:absolute;right:14px;top:10px}
  .btn-login{position:absolute;left:39px;top:456px;width:218px;height:30px;border-radius:15px;background:linear-gradient(180deg,var(--cyan),var(--violet));color:var(--white);font-size:9px;font-weight:700;text-align:center;line-height:30px}
  .forgot{position:absolute;top:504px;width:100%;text-align:center;font-size:9.5px;color:#555}
  .forgot i{display:inline-block;width:7px;height:7px;border:1px solid #555;margin-right:3px;vertical-align:-0.5px}
  .social{position:absolute;top:526px;width:100px;height:30px;border-radius:15px;border:2px solid var(--violet);border-right-color:var(--cyan);border-bottom-color:var(--cyan);background:var(--white);font-size:9.5px;color:#333;text-align:center;line-height:26px}

  /* About screen */
  .about{left:472px;background:linear-gradient(180deg,#05dbe9 0%,#3cb0f0 38%,#6d86f5 70%,#9a5cf6 100%)}
  .about__title{position:absolute;top:28px;width:100%;text-align:center;font-family:var(--head);font-weight:700;font-size:33px;color:var(--white)}
  .about__text{position:absolute;left:33px;width:229px;font-size:9.8px;line-height:19.6px;color:var(--white);text-align:justify;text-align-last:center}
  .about__photo{position:absolute;left:36px;top:326px;width:232px;height:324px;border-radius:110px 110px 0 0;background:linear-gradient(180deg,#6a4a3a 0%,#d89a6a 40%,#f4a024 70%,#f39a1e 100%);opacity:.9}

  /* Feed screen */
  .feed{left:834px;background:linear-gradient(180deg,#05dbe9 0%,#40aef1 40%,#7b7df5 70%,#a052f6 100%)}
  .tab{position:absolute;top:29px;width:79px;height:29px;border-radius:15px;font-family:var(--head);font-weight:600;font-size:12px;text-align:center;line-height:29px}
  .tab--active{left:64px;background:var(--violet);color:var(--white)}
  .tab--news{left:151px;background:#1c1c22;color:var(--white)}
  .challenge__title{position:absolute;top:100px;width:100%;text-align:center;font-family:var(--head);font-weight:600;font-size:22px;background:linear-gradient(90deg,#42c9f5,#b06cf8);-webkit-background-clip:text;background-clip:text;color:transparent}
  .challenge__text{position:absolute;left:45px;top:144px;width:205px;text-align:center;font-size:9.8px;line-height:17.3px;color:var(--white)}
  .btn-start{position:absolute;left:108px;top:218px;width:79px;height:29px;border-radius:15px;background:var(--cyan);color:var(--white);font-family:var(--head);font-weight:600;font-size:11.5px;text-align:center;line-height:29px}
  .stat{position:absolute;top:264px;width:111px;height:115px;border:2px solid var(--white);border-radius:8px;background:linear-gradient(180deg,#12cdec,#8a66f6);color:var(--white);padding:14px 0 0 15px}
  .stat__big{font-family:var(--head);font-weight:600;font-size:20px;line-height:24px}
  .stat__label{font-size:11px;font-weight:700;margin-top:2px}
  .stat__note{font-size:7px;font-weight:700;line-height:11px;margin-top:3px}
  .section{position:absolute;left:30px;top:398px;font-family:var(--head);font-weight:600;font-size:20px;color:var(--white)}
  .pill-more{position:absolute;left:222px;top:402px;width:43px;height:20px;border-radius:6px;background:var(--violet);color:var(--white);font-family:var(--head);font-weight:600;font-size:11.5px;text-align:center;line-height:20px}
  .brand-card{position:absolute;top:443px;width:107px;height:128px;border-radius:4px;background:var(--white);text-align:center}
  .brand-card--ghost{top:586px;height:80px;background:#b97ef7;opacity:.7}
  .avatar{position:absolute;left:22px;top:14px;width:63px;height:63px;border-radius:50%;background:#111;border:2.5px solid var(--violet);border-right-color:var(--cyan);border-bottom-color:var(--cyan)}
  .avatar--ghost{background:#a760f3;border-color:#c58af8;opacity:.8}
  .follow{position:absolute;left:34px;top:70px;width:39px;height:12px;border-radius:6px;background:var(--cyan);color:var(--white);font-family:var(--head);font-size:7px;line-height:12px}
  .brand-card__name{position:absolute;top:87px;width:100%;font-family:var(--head);font-weight:500;font-size:12.5px;color:#111}
  .brand-card__tags{position:absolute;top:106px;width:100%;font-family:var(--head);font-size:7.5px;color:#222}
  .more-toggle{position:absolute;left:135px;top:596px;width:24px;height:24px;border-radius:50%;background:var(--white)}
</style>
</head>
<body>

<!-- Login screen -->
<section class="screen login">
  <svg class="login__wave" width="295" height="300" viewBox="0 0 295 300">
    <defs>
      <linearGradient id="loginTop" x1="0" y1="0" x2="0" y2="1">
        <stop offset="0" stop-color="#44a3f0"/>
        <stop offset="1" stop-color="#a64af5"/>
      </linearGradient>
    </defs>
    <path d="M0 200 C40 270 140 310 295 255 V 230 L295 0 H0 Z" fill="#e6cff8"/>
    <path d="M0 170 C40 250 150 300 295 230 V0 H0 Z" fill="url(#loginTop)"/>
  </svg>
  <div class="login__brand">KIVORA</div>
  <h1 class="login__title">LOGIN</h1>
  <div class="field" style="top:372px">User name
    <svg width="8" height="9" viewBox="0 0 8 9"><circle cx="4" cy="2.5" r="2.2" fill="#888"/><path d="M0 9 C0 5 8 5 8 9Z" fill="#888"/></svg>
  </div>
  <div class="field" style="top:414px">Password
    <svg width="8" height="9" viewBox="0 0 8 9"><rect x="0.5" y="4" width="7" height="5" rx="1" fill="#888"/><path d="M2 4 V2.5 A2 2 0 0 1 6 2.5 V4" stroke="#888" fill="none"/></svg>
  </div>
  <div class="btn-login">LOGIN NOW</div>
  <div class="forgot"><i></i>Forget Password</div>
  <div class="social" style="left:39px">Loomby</div>
  <div class="social" style="left:157px">Pexaro</div>
</section>

<!-- About screen -->
<section class="screen about">
  <h2 class="about__title">ABOUT US</h2>
  <p class="about__text" style="top:92px">Lorem ipsum dolor sit amet, consectetur adipisc ing elit, sed do eiusmod tempor incididunt ut labore et dolore magna aliqua.Lorem ipsum dolor sit amet, consectetur adipisc ing elit, sed do eiusmod ut labore et dolore magna aliqua.</p>
  <p class="about__text" style="top:210px">Lorem ipsum dolor sit amet, consectetur adipisc ing elit, sed do eiusmod tempor incididunt ut labore et dolore magna aliqua.Lorem ipsum dolor sit amet, consectetur adipisc ing elit, sed do eiusmod ut labore et dolore magna aliqua.</p>
  <svg class="abs" style="left:0;top:330px" width="295" height="320" viewBox="0 0 295 320">
    <path d="M0 22 C110 -10 250 20 295 140 V320 H0 Z" fill="#2fc2ee" opacity=".55"/>
    <path d="M0 40 C110 10 230 50 280 160 L295 320 H0 Z" fill="#12d4ea" opacity=".6"/>
  </svg>
  <div class="about__photo" role="img" aria-label="Photo of a smiling young woman in an orange top holding a phone"></div>
</section>

<!-- Feed screen -->
<section class="screen feed">
  <div class="tab tab--active">FOR YOU</div>
  <div class="tab tab--news">NEWS</div>
  <svg class="abs" style="left:0;top:70px" width="295" height="300" viewBox="0 0 295 300">
    <defs>
      <radialGradient id="challengeGlow" cx="0.85" cy="0.7" r="0.8">
        <stop offset="0" stop-color="#f21ad0"/>
        <stop offset="0.45" stop-color="#7a0fb0"/>
        <stop offset="1" stop-color="#2a0a8a"/>
      </radialGradient>
    </defs>
    <circle cx="147" cy="149" r="146" fill="#7c4ff0"/>
    <circle cx="147" cy="149" r="143" fill="url(#challengeGlow)"/>
  </svg>
  <h3 class="challenge__title">Daily Challenge</h3>
  <p class="challenge__text">Lorem ipsum dolor sit amet, consectetur adi piscing elit, sed do eiusmod tempor incididu nt ut labore et dolore magna aliqua. Ut enim ad minim veniam</p>
  <div class="btn-start">START NOW</div>

  <div class="stat" style="left:30px">
    <div class="stat__big">Hey,<br>Robin!</div>
    <svg class="abs" style="left:15px;top:82px" width="90" height="22" viewBox="0 0 90 22">
      <text x="0" y="17" font-family="Oswald, sans-serif" font-weight="600" font-size="18" fill="#fff">8</text>
      <path d="M16 15 h14 l-2 -3 v-4 a5 5 0 0 0 -10 0 v4 z" fill="#fff"/>
      <circle cx="23" cy="17" r="2" fill="#fff"/>
      <circle cx="79" cy="12" r="8" fill="#fff"/>
      <path d="M77 8 l4 4 -4 4" stroke="#7b70f4" stroke-width="2" fill="none"/>
    </svg>
  </div>
  <div class="stat" style="left:149px">
    <div class="stat__big">$543</div>
    <div class="stat__label">Last earning</div>
    <div class="stat__big">$120</div>
    <div class="stat__note">Velo Advertisement<br>review</div>
  </div>

  <div class="section">Discover</div>
  <div class="pill-more">More</div>

  <div class="brand-card" style="left:31px">
    <div class="avatar"></div>
    <div class="follow">Follow</div>
    <div class="brand-card__name">Stride Co.</div>
    <div class="brand-card__tags">#sports &nbsp;#lifestyle</div>
  </div>
  <div class="brand-card" style="left:157px">
    <div class="avatar"></div>
    <div class="follow">Follow</div>
    <div class="brand-card__name">Kivora</div>
    <div class="brand-card__tags">#sports &nbsp;#lifestyle</div>
  </div>
  <div class="brand-card brand-card--ghost" style="left:31px"><div class="avatar avatar--ghost"></div></div>
  <div class="brand-card brand-card--ghost" style="left:157px"><div class="avatar avatar--ghost"></div></div>
  <div class="more-toggle">
    <svg width="24" height="24" viewBox="0 0 24 24"><path d="M9 10.5 l3 3 3 -3" stroke="#333" stroke-width="1.4" fill="none"/></svg>
  </div>
</section>

</body>
</html>
```